We need a business card design for a new soccer program based in Melbourne, Victoria, Australia.
Coaching kids from 2 through to 14 develop social, motor and soccer skills, in a fun and friendly non-competitive environment.
Our company colours are blue and orange as seen in the logo attached below. However, we are happy for the font to be any modern colour that looks professional.
Target Market(s)
Mums and dads
Industry/Entity Type
Business
Contact Information for Business Card
business name: Bright Kick Soccer
Marko Delvino Director- 0451 738 015
Luke Ferrano Director- 0419 856 371
Tomas Kovalenko Head Coach
email: marko@brightkicksoccer.com.au
website: www.brightkicksoccer.com.au
Coaching kids from 2-14
https://www.facebook.com/brightkicksoccer (facebook page not required unless it looks good without being clustered)
Look and feel

```html
<!DOCTYPE html>
<html lang="en">
<head>
<meta charset="utf-8">
<title>Bright Kick Soccer – Business Card</title>
<link rel="stylesheet" href="https://fonts.googleapis.com/css2?family=Exo+2:wght@400;500;800&display=swap">
<style>
  :root {
    --backdrop: #2b2b2b;
    --card-white: #f4f4f5;
    --card-shade: #e2e2e4;
    --brand-orange: #ff8200;
    --brand-blue: #0b1a9c;
    --ink-white: #ffffff;
  }
  html, body {
    margin: 0;
    padding: 0;
    width: 1200px;
    height: 889px;
    overflow: hidden;
    background: var(--backdrop);
    font-family: "Exo 2", "Segoe UI", sans-serif;
  }
  .stage {
    position: relative;
    width: 1200px;
    height: 889px;
  }
  .card {
    position: absolute;
    width: 580px;
    height: 330px;
    border-radius: 22px;
    overflow: hidden;
    background: radial-gradient(ellipse at 55% 50%, var(--card-white) 40%, var(--card-shade) 100%);
    box-shadow: 0 10px 24px rgba(0, 0, 0, 0.45);
  }
  .card--front { left: 190px; top: 80px; }
  .card--back { left: 420px; top: 470px; }

  .brand-name {
    font-weight: 800;
    color: var(--brand-blue);
    text-transform: uppercase;
    letter-spacing: 0.5px;
    line-height: 1;
    display: flex;
    align-items: center;
    gap: 12px;
  }
  .brand-dot {
    display: inline-block;
    border-radius: 50%;
    background: var(--brand-orange);
  }
  .card--front .brand-name {
    position: absolute;
    inset: 0;
    justify-content: center;
    font-size: 42px;
  }
  .card--front .brand-dot { width: 34px; height: 34px; }

  .back-art { position: absolute; inset: 0; }

  .card--back .brand-name {
    position: absolute;
    left: 330px;
    top: 92px;
    width: 230px;
    flex-direction: column;
    align-items: flex-start;
    font-size: 44px;
    gap: 4px;
  }
  .card--back .brand-name .word { display: block; }
  .card--back .brand-dot { width: 36px; height: 36px; margin-top: 6px; }

  .contact {
    position: absolute;
    left: 26px;
    top: 40px;
    width: 250px;
    color: var(--ink-white);
  }
  .contact__name {
    font-size: 18px;
    font-weight: 500;
    letter-spacing: 1px;
    text-transform: uppercase;
    margin: 0;
  }
  .contact__role {
    font-size: 13px;
    margin: 2px 0 0;
  }
  .contact__address {
    font-size: 13px;
    line-height: 1.45;
    margin: 44px 0 34px;
  }
  .contact__list {
    list-style: none;
    margin: 0;
    padding: 0;
    font-size: 12px;
  }
  .contact__list li {
    display: flex;
    align-items: center;
    gap: 9px;
    height: 23px;
    white-space: nowrap;
  }
  .contact__list svg {
    width: 14px;
    height: 14px;
    fill: var(--ink-white);
    flex: none;
  }
</style>
</head>
<body>
<main class="stage">

  <section class="card card--front" aria-label="Card front">
    <div class="brand-name"><span>Bright Kick Soccer</span><span class="brand-dot"></span></div>
  </section>

  <section class="card card--back" aria-label="Card back">
    <svg class="back-art" viewBox="0 0 580 330" preserveAspectRatio="none" aria-hidden="true">
      <path d="M0 0 H278 C250 90 255 230 310 330 H0 Z" fill="var(--brand-orange)"/>
      <path d="M292 0 C262 90 268 230 326 330" fill="none" stroke="var(--brand-blue)" stroke-width="7"/>
    </svg>

    <div class="contact">
      <p class="contact__name">Marko Delvino</p>
      <p class="contact__role">Director</p>
      <p class="contact__address">Coaching kids from 2-14<br>Melbourne, Victoria</p>
      <ul class="contact__list">
        <li>
          <svg viewBox="0 0 16 16"><path d="M3.5 1.5l2.5 3-1.5 1.8c.9 1.9 2.3 3.3 4.2 4.2L10.5 9l3 2.5-1.2 2.6C7 14 2 9 1.9 3.7z"/></svg>
          0451 738 015
        </li>
        <li>
          <svg viewBox="0 0 16 16"><path d="M1 3h14v10H1zM2.5 4.5v.4L8 8.8l5.5-3.9v-.4zM2.5 6.7v4.8h11V6.7L8 10.6z"/></svg>
          marko@brightkicksoccer.com.au
        </li>
        <li>
          <svg viewBox="0 0 16 16"><path d="M8 1a7 7 0 1 0 0 14A7 7 0 0 0 8 1zm0 1.5c.8 0 1.7 1.5 2 3.8H6c.3-2.3 1.2-3.8 2-3.8zM5.2 3.1c-.4.9-.6 2-.7 3.2H2.7a5.6 5.6 0 0 1 2.5-3.2zm5.6 0a5.6 5.6 0 0 1 2.5 3.2h-1.8c-.1-1.2-.3-2.3-.7-3.2zM2.7 7.7h1.8c.1 1.2.3 2.3.7 3.2a5.6 5.6 0 0 1-2.5-3.2zm3.3 0h4c-.3 2.3-1.2 3.8-2 3.8s-1.7-1.5-2-3.8zm5.5 0h1.8a5.6 5.6 0 0 1-2.5 3.2c.4-.9.6-2 .7-3.2z"/></svg>
          www.brightkicksoccer.com.au
        </li>
      </ul>
    </div>

    <div class="brand-name">
      <span class="word">Bright</span>
      <span class="word">Kick</span>
      <span class="word">Soccer</span>
      <span class="brand-dot"></span>
    </div>
  </section>

</main>
</body>
</html>
```